PowerPoint Presentation

We are looking for a new PPT layout template existing of a cover page, three internal pages - one with text bullets, one with a picture/information and one with more of a table for pricing information and the last a last "thank you - contact info" page. Feel free to grab any graphics from our website at www.brightharbor.com

Any product can be chosen from our products page. Colors are cyan and orange and feel free to choose darker backgrounds for the front and end page. Also included in the graphics is our new business card design.

Also note we are updating our website, and have attached a sample of how it looks for reference.

Reason: We are still looking for submissions for our PowerPoint presentation. We have increased the award amount as well.

Target Market(s)

Target market is private industry professionals, public safety organizations, and state and local government agencies.

Industry/Entity Type

Business

Colors
33a6d7
86cae6
cee9f5
f68d4d
f8ba93
fce2d4

```html
<!DOCTYPE html>
<html lang="en">
<head>
<meta charset="utf-8">
<title>Bright Harbor — Presentation Cover</title>
<link rel="stylesheet" href="https://fonts.googleapis.com/css2?family=Arimo:wght@400;700&family=Open+Sans:wght@400&display=swap">
<style>
  :root {
    --cyan: #29b6f5;
    --orange: #ed9566;
    --ink: #1d2f41;
    --black: #0d0d0e;
    --white: #ffffff;
    --gold: #f5d24a;
  }
  * { margin: 0; padding: 0; box-sizing: border-box; }
  html, body {
    width: 1200px;
    height: 900px;
    overflow: hidden;
    background: var(--black);
  }
  .slide {
    position: relative;
    width: 1200px;
    height: 900px;
    font-family: "Arimo", Arial, sans-serif;
  }
  .masthead {
    position: absolute;
    top: 0; left: 0;
    width: 100%;
    height: 131px;
    background: var(--cyan);
    display: flex;
    align-items: center;
    justify-content: center;
    gap: 20px;
    padding-bottom: 6px;
  }
  .brand-dot {
    width: 34px;
    height: 34px;
    border-radius: 50%;
    background: var(--ink);
  }
  .brand-name {
    font-weight: 700;
    font-size: 47px;
    letter-spacing: 1px;
    color: var(--ink);
  }
  .header-rule {
    position: absolute;
    top: 131px; left: 0;
    width: 100%;
    height: 35px;
    background: var(--black);
  }
  .cover {
    position: absolute;
    top: 166px; left: 0;
    width: 100%;
    height: 654px;
    background: var(--orange);
  }
  .cover-title {
    position: absolute;
    top: 212px; left: 0;
    width: 100%;
    text-align: center;
    font-weight: 700;
    font-size: 66px;
    letter-spacing: 0.5px;
    color: var(--ink);
  }
  .cover-subtitle {
    position: absolute;
    top: 338px; left: 0;
    width: 100%;
    text-align: center;
    font-family: "Open Sans", "Segoe UI", sans-serif;
    font-weight: 400;
    font-size: 50px;
    color: var(--ink);
  }
  .footer-rule {
    position: absolute;
    top: 820px; left: 0;
    width: 100%;
    height: 8px;
    background: var(--white);
  }
  .footer {
    position: absolute;
    top: 828px; left: 0;
    width: 100%;
    height: 72px;
    background: var(--black);
    color: var(--gold);
    font-size: 27px;
  }
  .footer span {
    position: absolute;
    top: 22px;
  }
  .footer-date { left: 23px; }
  .footer-presenter {
    left: 0; width: 100%;
    text-align: center;
    font-weight: 700;
  }
  .footer-role { right: 23px; }
</style>
</head>
<body>
  <main class="slide">
    <header class="masthead">
      <span class="brand-dot" aria-hidden="true"></span>
      <span class="brand-name">BRIGHT HARBOR</span>
    </header>
    <div class="header-rule"></div>

    <section class="cover">
      <h1 class="cover-title">PRESENTATION TITLE</h1>
      <p class="cover-subtitle">Presentation Subtitle</p>
    </section>

    <div class="footer-rule"></div>
    <footer class="footer">
      <span class="footer-date">03 March 2014</span>
      <span class="footer-presenter">PRESENTOR’S NAME</span>
      <span class="footer-role">Job Title</span>
    </footer>
  </main>
</body>
</html>
```